Packaging design for Lumo Drift Style snack

Looking for food product packaging. Our product is a sweet, salty, and savory lumo drift style snack. We would like to see designs that use the colors yellow and red and any color that compliments them is welcomed. Preferably pastel if possible to be more modern contemporary but with an appeal to kids to young adults. The final design should communicate spark curiosity, hunger, and addiction.

Target Market(s)

12 - 60 year olds. Mainly targeting younger kids but also to older adults

Industry/Entity Type

Food & Beverage

Colors
FFF300
FFF600
FEFA6F
FFFEC7
FFFEE8
FFC000
F8CF3A
FAE287
FDF2CF
FEFAEE
F0912C
F2A743
F7CA91
FBE8D2
FDF5EE
EE7325
F08F49
F5BC92
FAE3D3
FDF4ED

```html
<!DOCTYPE html>
<html lang="en">
<head>
<meta charset="utf-8">
<title>Zesto Bitz – Cereal Mix Pouch</title>
<link rel="stylesheet" href="https://fonts.googleapis.com/css2?family=Montserrat:wght@400;600;800;900&family=Amatic+SC:wght@700&family=Patrick+Hand&display=swap">
<style>
  :root{
    --red:#c9303f;
    --red-deep:#b1273a;
    --gold:#f2d98d;
    --gold-light:#f8e7ae;
    --gold-dark:#e4c670;
    --cream:#fdf2cf;
    --ink:#2a2320;
    --white:#ffffff;
    --bg:#ffffff;
  }
  *{box-sizing:border-box;margin:0;padding:0}
  html,body{width:1200px;height:1000px;overflow:hidden;background:var(--bg)}
  .canvas{position:relative;width:1200px;height:1000px;font-family:"Montserrat",sans-serif;color:var(--ink)}

  .pouch{position:absolute;top:110px;width:480px;height:780px;border-radius:14px;overflow:hidden;
    background:linear-gradient(160deg,var(--gold-light),var(--gold) 45%,var(--gold-dark));}
  .pouch--front{left:95px}
  .pouch--back{left:625px}
  .pouch__seal{position:absolute;left:0;top:0;width:100%;height:125px;
    background:linear-gradient(180deg,#d8485a,var(--red) 60%,var(--red-deep));}
  .pouch__zip{position:absolute;left:0;top:92px;width:100%;height:6px;background:rgba(0,0,0,.12)}

  /* front */
  .brand{position:absolute;font-weight:900;color:var(--red);line-height:.9;letter-spacing:-1px;text-align:center}
  .pouch--front .brand{left:0;width:100%;top:175px}
  .brand__main{display:block;font-size:86px}
  .brand__sub{display:block;font-size:44px;margin-top:6px}
  .brand__dot{position:absolute;left:58px;top:80px;width:58px;height:58px;border-radius:50%;background:var(--red)}

  .tagline{position:absolute;left:0;width:100%;top:335px;text-align:center;font-family:"Amatic SC",cursive;
    font-weight:700;font-size:50px;color:var(--red);letter-spacing:1px}
  .tagline__rule{position:absolute;left:70px;top:396px;width:340px;height:4px;background:var(--red);border-radius:2px}

  .bowl{position:absolute;border-radius:50%;border:18px solid #d94a57;
    box-shadow:0 0 0 6px rgba(201,48,63,.35)}
  .bowl__food{width:100%;height:100%;border-radius:50%;
    background:radial-gradient(circle at 40% 40%,#f1ead8,#c99a62 45%,#8a5a34 80%,#5e3b22)}
  .pouch--front .bowl{left:95px;top:425px;width:290px;height:290px}

  .label-pill{position:absolute;left:135px;top:722px;width:190px;height:38px;border-radius:8px;background:var(--red);
    border:3px solid var(--white);outline:2px solid var(--red);
    font-family:"Patrick Hand",cursive;font-size:24px;color:var(--white);text-align:center;line-height:32px;letter-spacing:1px}
  .netwt{position:absolute;left:365px;top:690px;width:62px;height:62px;border-radius:12px;background:var(--red);
    font-family:"Patrick Hand",cursive;color:var(--white);font-size:13px;line-height:1.1;text-align:center;padding-top:14px;transform:rotate(-6deg)}

  .spot{position:absolute;border-radius:50%;background:var(--white);border:3px solid var(--red)}

  /* back */
  .pouch--back .brand{left:30px;top:150px;text-align:left}
  .pouch--back .brand__main{font-size:54px}
  .pouch--back .brand__sub{font-size:28px;margin-left:40px}
  .copy{position:absolute;font-size:8.5px;line-height:1.35;color:#4a3f32}
  .copy--intro{left:30px;top:245px;width:420px}
  .copy--intro p+p{margin-top:6px}
  .copy--side{left:270px;top:305px;width:180px;text-align:justify}
  .bullets{position:absolute;left:270px;top:368px;width:180px;list-style:none;font-size:8px;line-height:1.3;color:#4a3f32}
  .bullets li{position:relative;padding-left:14px;margin-bottom:6px}
  .bullets li::before{content:"";position:absolute;left:0;top:3px;width:6px;height:6px;border-radius:50%;background:var(--white)}

  .facts{position:absolute;left:30px;top:320px;width:215px;font-size:10.5px;font-weight:600}
  .facts__title{font-size:21px;font-weight:800;border-bottom:5px solid var(--ink);padding-bottom:4px}
  .facts__row{display:flex;justify-content:space-between;border-bottom:1px solid var(--ink);padding:5px 0}
  .facts__row--thick{border-bottom-width:4px}
  .pouch--back .bowl{left:262px;top:505px;width:180px;height:180px;border-width:12px}

  .icons{position:absolute;left:70px;top:720px;display:flex;gap:18px;align-items:flex-end}
  .url{position:absolute;left:265px;top:730px;width:170px;height:22px;border-radius:11px;background:var(--red);
    color:var(--white);font-size:10px;font-weight:800;text-align:center;line-height:22px}
</style>
</head>
<body>
<div class="canvas">

  <section class="pouch pouch--front" aria-label="Front of pouch">
    <div class="pouch__seal"></div><div class="pouch__zip"></div>
    <span class="spot" style="left:40px;top:300px;width:16px;height:16px"></span>
    <span class="spot" style="left:420px;top:180px;width:14px;height:14px"></span>
    <span class="spot" style="left:35px;top:560px;width:18px;height:18px"></span>
    <span class="spot" style="left:430px;top:600px;width:14px;height:14px"></span>
    <span class="brand__dot"></span>
    <h1 class="brand"><span class="brand__main">Zesto</span><span class="brand__sub">Bitz</span></h1>
    <p class="tagline">Addicted to Happiness</p>
    <div class="tagline__rule"></div>
    <div class="bowl"><div class="bowl__food" role="img" aria-label="Bowl of crunchy cereal snack mix with pretzels and rye chips"></div></div>
    <div class="label-pill">CEREAL MIX</div>
    <div class="netwt">NET WT<br>250G</div>
  </section>

  <section class="pouch pouch--back" aria-label="Back of pouch">
    <div class="pouch__seal"></div><div class="pouch__zip"></div>
    <h2 class="brand"><span class="brand__main">Zesto</span><span class="brand__sub">Bitz</span></h2>
    <div class="copy copy--intro">
      <p>Lorem ipsum dolor sit amet, consectetuer adipiscing elit, sed diam nonummy nibh euismod tincidunt ut laoreet dolore magna aliquam erat volutpat. Ut wisi enim ad minim veniam, quis nostrud exerci tation ullamcorper suscipit lobortis nisl ut aliquip ex ea commodo consequat.</p>
      <p>Ut wisi enim ad minim veniam, quis nostrud exerci tation ullamcorper suscipit lobortis nisl ut aliquip ex ea commodo consequat.</p>
    </div>
    <div class="facts">
      <div class="facts__title">Nutrition Facts</div>
      <div class="facts__row facts__row--thick"><span>Serving Size 30g</span><span></span></div>
      <div class="facts__row"><span>Calories 120</span><span>Calories from fat 12</span></div>
      <div class="facts__row"><span></span><span>% Daily Value</span></div>
      <div class="facts__row"><span>Total Fat 2g</span><span>4%</span></div>
      <div class="facts__row"><span>Saturated Fat 1g</span><span>4%</span></div>
      <div class="facts__row"><span>Trans Fat 0g</span><span></span></div>
      <div class="facts__row"><span>Cholesterol 0mg</span><span>0%</span></div>
      <div class="facts__row"><span>Sodium 0mg</span><span>0%</span></div>
      <div class="facts__row"><span>Total Carbohydrate 19g</span><span>3%</span></div>
      <div class="facts__row"><span>Dietary Fiber 2g</span><span>6%</span></div>
      <div class="facts__row facts__row--thick"><span>Protein 3g</span><span></span></div>
      <div class="facts__row"><span>Vitamin A 20%</span><span></span></div>
      <div class="facts__row"><span>Zinc 5%</span><span></span></div>
    </div>
    <p class="copy copy--side">Lorem ipsum dolor sit amet, consectetuer adipiscing elit, sed diam nonummy nibh euismod tincidunt ut laoreet dolore magna aliquam erat volutpat.</p>
    <ul class="bullets">
      <li>Lorem ipsum dolor sit amet, consectetuer adipiscing elit.</li>
      <li>Sed diam nonummy nibh euismod tincidunt ut laoreet.</li>
      <li>Dolore magna aliquam erat volutpat.</li>
      <li>Ut wisi enim ad minim veniam, quis nostrud exerci tation ullamcorper.</li>
      <li>Suscipit lobortis nisl ut aliquip ex ea commodo consequat.</li>
    </ul>
    <div class="bowl"><div class="bowl__food" role="img" aria-label="Bowl of cereal snack mix"></div></div>
    <div class="icons" aria-label="Recycling and disposal icons">
      <svg width="40" height="36" viewBox="0 0 40 36" aria-hidden="true">
        <path d="M20 3 L34 30 H6 Z" fill="none" stroke="var(--red)" stroke-width="5" stroke-linejoin="round"/>
      </svg>
      <svg width="24" height="30" viewBox="0 0 24 30" aria-hidden="true">
        <rect x="2" y="4" width="20" height="4" fill="var(--red)"/>
        <path d="M4 10 H20 L18 29 H6 Z" fill="var(--red)"/>
      </svg>
      <svg width="32" height="36" viewBox="0 0 32 36" aria-hidden="true">
        <circle cx="18" cy="5" r="4" fill="var(--red)"/>
        <path d="M18 11 L14 22 L8 34 M14 22 L20 34 M16 14 L26 18 M16 14 L8 12" stroke="var(--red)" stroke-width="4" fill="none" stroke-linecap="round"/>
      </svg>
    </div>
    <div class="url">www.yoursite.com</div>
  </section>

</div>
</body>
</html>
```